Belvanta - Awnings & Outdoor Blinds

We need a brochure design for out Australia based Awnings & Outdoor Blinds company.

We require 2 templates:

1. Product Specific. (For One Product) - Single or Double Sided A4
Must Include:
Our Logo, Product Description, Pictures,Product Features & Benefits (in point form) & Our Contact Details (Phone & Website).

2.Product Range (Our Full Range) - 8 Page A4 (2x A3 Folded In Half Printed Both Sides).
Must Include:
Page 1 - Front Cover - Title (Product Range) Cover With Our Logo & Photo/s.
Page 2 - About Us, Why Us & Warranty Information.
Page 3 - A Gallery (Just Photos Showcasing Our Work)
Page 4 - 3 Products Per Page (Image/s, Product Title & Brief Description).
Page 5 - 3 Products Per Page (Image/s, Product Title & Brief Description).
Page 6 - 3 Products Per Page (Image/s, Product Title & Brief Description).
Page 7 - 3 Products Per Page (Image/s, Product Title & Brief Description).
Page 8 - Back Cover with our Contact Details (Phone, Website & Logo).

We are just looking for templates we will fill in all the content, needs to be easy to customise (change photos/text etc).

For more info on what we do: http://site7305.example-builder.com/belvanta

Requirements
Nice to have
• Nice to have the product pages 4 - 7 not as identical layout.

Nice to be in our colours Red, White, Black, Light Grey. (See Logo Variations - Logo is the top one).

```html
<!DOCTYPE html>
<html lang="en">
<head>
<meta charset="utf-8">
<title>Belvanta – Product Range, Pages 6–7</title>
<link rel="stylesheet" href="https://fonts.googleapis.com/css2?family=Exo+2:wght@400;600;700&display=swap">
<style>
  :root{
    --red:#c3162a;
    --red-dark:#9e0f1f;
    --red-light:#dc3a4c;
    --black:#1b1b1b;
    --grey:#e9e9e9;
    --page:#ffffff;
    --ink:#4a4a4a;
    --stage:#dcdcdc;
  }
  *{box-sizing:border-box;margin:0;padding:0}
  html,body{width:1200px;height:847px;overflow:hidden}
  body{background:var(--stage);font-family:"Exo 2",sans-serif;color:var(--ink)}
  .spread{position:absolute;left:40px;top:30px;width:1120px;height:787px;display:flex;
    box-shadow:0 6px 24px rgba(0,0,0,.18)}
  .page{position:relative;width:560px;height:787px;background:var(--page);padding:24px 26px 16px;overflow:hidden}
  .page--left{border-right:1px solid #d6d6d6}
  .product{position:relative;height:245px;margin-bottom:2px}
  .product__band{position:absolute;left:0;right:0;top:0;height:32px;
    background:linear-gradient(90deg,var(--red-dark),var(--red) 40%,var(--red-light));
    display:flex;align-items:center}
  .product__tab{height:32px;padding:0 7px;background:var(--black);color:#fff;
    font-size:9px;font-weight:600;display:flex;align-items:center;letter-spacing:.02em}
  .product__title{color:#fff;font-weight:700;font-size:19px;padding-left:12px;letter-spacing:.01em}
  .product__hero{position:absolute;left:0;top:40px;width:222px;height:170px}
  .product__body{position:absolute;left:236px;right:0;top:42px}
  .product__text{font-size:10.5px;line-height:1.42;text-align:justify}
  .product__thumbs{display:flex;gap:6px;margin-top:12px}
  .thumb{flex:1;height:70px}
  .product--motor .product__text{font-size:10px;line-height:1.32}
  .product--motor .product__thumbs{margin-top:8px}
  .product--motor .thumb{height:52px}
  .photo{display:block}
  .tone-stone{background:linear-gradient(160deg,#d9d2c3,#8c8679 60%,#5f5a50)}
  .tone-patio{background:linear-gradient(180deg,#b9c7d3,#9a8e7c 55%,#6b5e4b)}
  .tone-dusk{background:linear-gradient(180deg,#3c5f93,#25344c 55%,#4f6b35)}
  .tone-garden{background:linear-gradient(180deg,#c9d7e0,#7e8b6c 60%,#4e5c3b)}
  .tone-house{background:linear-gradient(180deg,#bfc9cf,#ece7df 50%,#9c9486)}
  .tone-terra{background:linear-gradient(160deg,#e7e1d6,#b8735a 55%,#7d4c3a)}
  .tone-cafe{background:linear-gradient(180deg,#8a2332,#6b1f28 50%,#3f5b2f)}
  .tone-mesh{background:linear-gradient(180deg,#4a4d52,#2f3135)}
  .tone-sand{background:linear-gradient(180deg,#d9c5a3,#b49670)}
  .tone-facade{background:linear-gradient(180deg,#6e94c6,#c9b48a 45%,#8e7a5a)}
  .tone-pool{background:linear-gradient(180deg,#78a7d6,#e2d9c8 55%,#5aa0c6)}
  .tone-white{background:linear-gradient(160deg,#fafafa,#dcdcdc)}
  .tone-white2{background:linear-gradient(160deg,#f2f2f2,#cfcfcf)}
</style>
</head>
<body>
<main class="spread">

  <section class="page page--left">
    <article class="product">
      <div class="product__band"><span class="product__tab">Belvanta</span><h2 class="product__title">Wire Guided</h2></div>
      <div class="photo product__hero tone-stone" role="img" aria-label="Photo of a wire guided outdoor blind lowered over a stone patio"></div>
      <div class="product__body">
        <p class="product__text">Wire guide awnings offer functionality, style and control, combining a heavy duty crank operated gearbox guided by stainless steel wire and fittings that feed in the weighted aluminium bottom rail of the blind allowing for precision movement, no unwanted warping or flapping, giving you the flexibility to stop the blind at any vertical position.</p>
        <div class="product__thumbs">
          <div class="photo thumb tone-mesh" role="img" aria-label="Photo of a dark wire guided blind on a veranda"></div>
          <div class="photo thumb tone-garden" role="img" aria-label="Photo of a blind on a house corner"></div>
          <div class="photo thumb tone-house" role="img" aria-label="Photo of a pale blind on a modern home"></div>
        </div>
      </div>
    </article>

    <article class="product">
      <div class="product__band"><span class="product__tab">Belvanta</span><h2 class="product__title">Drop Arm Awnings</h2></div>
      <div class="photo product__hero tone-patio" role="img" aria-label="Photo of drop arm awnings over windows beside a patio lounger"></div>
      <div class="product__body">
        <p class="product__text">Designed to deflect heat and glare while maximising light, ventilation and privacy within the home. The inclination of the drop-arm awning provides precisely the right angle to allow for shade where needed while permitting sufficient light and airflow. The spring loaded arms provide tension for improved wind performance.</p>
        <div class="product__thumbs">
          <div class="photo thumb tone-sand" role="img" aria-label="Photo of striped drop arm awnings"></div>
          <div class="photo thumb tone-house" role="img" aria-label="Photo of awnings on a white house"></div>
          <div class="photo thumb tone-terra" role="img" aria-label="Photo of a red drop arm awning"></div>
        </div>
      </div>
    </article>

    <article class="product">
      <div class="product__band"><span class="product__tab">Belvanta</span><h2 class="product__title">Cafe Blinds</h2></div>
      <div class="photo product__hero tone-dusk" role="img" aria-label="Photo of a glass-enclosed veranda with cafe blinds at dusk"></div>
      <div class="product__body">
        <p class="product__text">Our Cafe Blinds are fixed at the top by aluminium sail track, this drop blind can be manually rolled up and down using the rope and pulley. The rope loops around a bottom bar on the left and right of the blind and is then attached to a pulley on one side. This is the ideal solution for the sloping veranda roof where no other systems can be used.</p>
        <div class="product__thumbs">
          <div class="photo thumb tone-garden" role="img" aria-label="Photo of an outdoor dining area with cafe blinds"></div>
          <div class="photo thumb tone-house" role="img" aria-label="Photo of a covered terrace with clear blinds"></div>
          <div class="photo thumb tone-patio" role="img" aria-label="Photo of a pergola with cafe blinds"></div>
        </div>
      </div>
    </article>
  </section>

  <section class="page page--right">
    <article class="product">
      <div class="product__band"><span class="product__tab">Belvanta</span><h2 class="product__title">Fixed Fabric Pannels &amp; Infills</h2></div>
      <div class="photo product__hero tone-cafe" role="img" aria-label="Photo of red fixed fabric panels on a cafe building among trees"></div>
      <div class="product__body">
        <p class="product__text">Fixed Panels are constructed with an aluminium frame and are available in a wide range of durable fabrics. They are customised for other applications such as doors, windows and any area where a retractable blind is not required.</p>
        <div class="product__thumbs">
          <div class="photo thumb tone-mesh" role="img" aria-label="Photo of a dark fixed fabric panel"></div>
          <div class="photo thumb tone-terra" role="img" aria-label="Photo of fabric infills on a timber fence"></div>
          <div class="photo thumb tone-sand" role="img" aria-label="Photo of beige fabric panels"></div>
        </div>
      </div>
    </article>

    <article class="product">
      <div class="product__band"><span class="product__tab">Belvanta</span><h2 class="product__title">Folding Arm Awnings</h2></div>
      <div class="photo product__hero tone-facade" role="img" aria-label="Photo of red folding arm awnings on a two-storey stone building"></div>
      <div class="product__body">
        <p class="product__text">Our folding arm awnings incorporate innovative new designs, reflecting today's demands for function, design and construction. These awnings are discreet, timeless designs that fit seamlessly in every setting, and can be neatly rolled away when not in use.</p>
        <div class="product__thumbs">
          <div class="photo thumb tone-pool" role="img" aria-label="Photo of a folding arm awning by a pool"></div>
          <div class="photo thumb tone-house" role="img" aria-label="Photo of an awning over an outdoor setting"></div>
          <div class="photo thumb tone-garden" role="img" aria-label="Photo of an awning on a garden terrace"></div>
        </div>
      </div>
    </article>

    <article class="product product--motor">
      <div class="product__band"><span class="product__tab">Belvanta</span><h2 class="product__title">Motorise My Blinds</h2></div>
      <div class="photo product__hero tone-white" role="img" aria-label="Product shot of a blind motor with wind sensor"></div>
      <div class="product__body">
        <p class="product__text">Awnings and Outdoor Blinds fitted with an electric motor are as easy and comfortable to use as a touch of a button. What's more, automatic control provides continuous protection, as the awning or screen automatically extends or retracts according to the weather. The motor fits discreetly into the fabric roller tube, well out of sight. What you will see is the wall mounted switch or hand held remote control. Furthermore, motorisation eliminates the use of cranks or tapes that look unattractive. When the motor is in operation, it is whisper quiet.</p>
        <div class="product__thumbs">
          <div class="photo thumb tone-white2" role="img" aria-label="Product shot of a wall mounted switch"></div>
          <div class="photo thumb tone-white" role="img" aria-label="Product shot of hand held remote controls"></div>
        </div>
      </div>
    </article>
  </section>

</main>
</body>
</html>
```